LedgerNook Project
LedgerNook
Project: LedgerNook Project
LedgerNook Project - Financial Services
Creative Brief
Bright & Fun-filled
Peter Halvik
President
Leave blank
peter@ledgernook.example
www.ledgernook.example
The front should be white with logo, my name, cell phone, email address, and website. Leave address blank because there is no physical address at the moment. List these services with bullet point. (accounting, bookkeeping, and payroll) Please make sure the design meet GlossPrint silk laminate with spot uv because I plan to use them to print in the future. Check link: http://www.glossprint.example/Business-Cards/Silk-Business-Cards-with-Spot-UV-and-Rounded-Corners
I want the back to be a solid color with logo. Check link for what I am looking for: http://www.glossprint.example/Inspiration-Gallery#/gallery/img/images_M.jpg

```html
<!DOCTYPE html>
<html lang="en">
<head>
<meta charset="utf-8">
<title>LedgerNook Business Cards</title>
<link rel="stylesheet" href="https://fonts.googleapis.com/css2?family=Open+Sans:wght@400;600;700&display=swap">
<style>
  :root {
    --backdrop: #eeeae4;
    --card-white: #ffffff;
    --brand-blue: #1f86d6;
    --brand-blue-light: #5cb2f0;
    --brand-navy: #17375e;
    --ink: #2a2a2a;
    --soft-white: rgba(255,255,255,0.18);
  }
  html, body {
    margin: 0;
    padding: 0;
    width: 1200px;
    height: 773px;
    overflow: hidden;
    background: var(--backdrop);
    font-family: "Open Sans", Arial, sans-serif;
  }
  .canvas {
    position: relative;
    width: 1200px;
    height: 773px;
  }
  .card {
    position: absolute;
    width: 515px;
    height: 296px;
    border-radius: 22px;
    overflow: hidden;
    box-shadow: 0 4px 10px rgba(0,0,0,0.18);
    background: var(--card-white);
  }
  .card--front { left: 343px; top: 67px; }
  .card--plain { left: 72px; top: 403px; }
  .card--back  { left: 619px; top: 403px;
    background: linear-gradient(180deg, var(--brand-blue-light) 0%, var(--brand-blue) 100%); }

  .brand {
    position: absolute;
    left: 0; right: 0;
    display: flex;
    flex-direction: column;
    align-items: center;
  }
  .brand__mark {
    width: 48px;
    height: 48px;
    background: var(--brand-blue);
  }
  .brand__name {
    margin-top: 6px;
    font-weight: 700;
    font-size: 26px;
    color: var(--brand-navy);
    letter-spacing: -0.5px;
    line-height: 1;
  }
  .card--front .brand { top: 20px; }
  .card--plain .brand { top: 40px; }

  .contact-band {
    position: absolute;
    left: 0; right: 0;
    top: 144px;
    height: 106px;
    background: linear-gradient(180deg, var(--brand-blue) 0%, var(--brand-blue-light) 100%);
    color: #fff;
    text-align: center;
    display: flex;
    flex-direction: column;
    justify-content: center;
  }
  .contact-band__name {
    font-weight: 700;
    font-size: 19px;
    line-height: 1.2;
  }
  .contact-band__title {
    font-size: 12.5px;
    line-height: 1.3;
    margin-bottom: 6px;
  }
  .contact-band__line {
    font-size: 12.5px;
    line-height: 1.4;
  }

  .services {
    position: absolute;
    left: 0; right: 0;
    top: 260px;
    margin: 0; padding: 0;
    list-style: none;
    display: flex;
    justify-content: center;
    gap: 8px;
    font-size: 15px;
    font-weight: 600;
    color: var(--ink);
  }
  .services li + li::before {
    content: "\2022";
    margin-right: 8px;
  }

  .website {
    position: absolute;
    left: 0; right: 0;
    bottom: 22px;
    text-align: center;
    font-size: 13px;
    letter-spacing: 2px;
    color: var(--ink);
  }
  .card--back .website { color: #fff; }

  .back-mark {
    position: absolute;
    left: 182px;
    top: 40px;
    width: 150px;
    height: 150px;
    background: var(--soft-white);
  }
</style>
</head>
<body>
<main class="canvas">

  <section class="card card--front" aria-label="Card front">
    <div class="brand">
      <div class="brand__mark"></div>
      <div class="brand__name">LedgerNook</div>
    </div>
    <div class="contact-band">
      <div class="contact-band__name">Peter Halvik</div>
      <div class="contact-band__title">President</div>
      <div class="contact-band__line">Cell: 555-010-2377</div>
      <div class="contact-band__line">Email: peter@ledgernook.example</div>
    </div>
    <ul class="services">
      <li>Accounting</li>
      <li>Bookkeeping</li>
      <li>Payroll</li>
    </ul>
  </section>

  <section class="card card--plain" aria-label="Card front, alternate">
    <div class="brand">
      <div class="brand__mark"></div>
      <div class="brand__name">LedgerNook</div>
    </div>
    <div class="website">www.ledgernook.example</div>
  </section>

  <section class="card card--back" aria-label="Card back">
    <div class="back-mark"></div>
    <div class="website">www.ledgernook.example</div>
  </section>

</main>
</body>
</html>
```